Concierge Healthcare Business Card Design and Logo

We need a logo and business card design for a new company called "Sound Keeper". We will provide concierge audiological care, hearing aids, hearing exams, custom hearing protection etc to patients in the comfort of their homes and offices. We would like a sleek and modern design preferably with an Ear related logo.

Target Market(s)

People with hearing loss, Hunters, Musicians
My usual clientele are older individuals so usually 50+ years old

Industry/Entity Type

Health Care

Contact Information for Business Card

Clara Whitfield, AuD
Audiologist
512-418-2967
soundkeeper@mailvista.net
www.soundkeeperclinic.net

Logo Text

Sound Keeper

Number of Pages Required

3 page

```html
<!DOCTYPE html>
<html lang="en">
<head>
<meta charset="UTF-8">
<title>Sound Keeper — Business Cards</title>
<link rel="stylesheet" href="https://fonts.googleapis.com/css2?family=Montserrat:wght@400;600;700&display=swap">
<style>
  :root {
    --backdrop: #2b2b2d;
    --card-black: #050505;
    --card-white: #ffffff;
    --ink: #111111;
    --ink-soft: #2a2a2a;
    --accent-blue: #1ea0e0;
    --divider: #3a3a3a;
    --card-radius: 22px;
  }
  * { box-sizing: border-box; margin: 0; padding: 0; }
  html, body {
    width: 1200px;
    height: 900px;
    overflow: hidden;
    background: var(--backdrop);
    font-family: "Montserrat", sans-serif;
  }
  .canvas {
    position: relative;
    width: 1200px;
    height: 900px;
  }
  .card {
    position: absolute;
    width: 560px;
    height: 320px;
    border-radius: var(--card-radius);
    box-shadow: 0 18px 40px rgba(0, 0, 0, 0.45);
  }
  .card--front {
    left: 100px;
    top: 110px;
    background: var(--card-black);
    display: flex;
    align-items: center;
    justify-content: center;
  }
  .card--back {
    left: 540px;
    top: 470px;
    background: var(--card-white);
    display: flex;
    align-items: center;
    padding: 0 36px 0 40px;
  }
  .brand {
    display: flex;
    align-items: center;
    gap: 14px;
  }
  .brand__dot {
    width: 34px;
    height: 34px;
    border-radius: 50%;
    background: var(--accent-blue);
    flex: none;
  }
  .brand__name {
    font-weight: 700;
    font-size: 40px;
    letter-spacing: 0.5px;
    color: #ffffff;
  }
  .card--back .brand {
    width: 230px;
    flex: none;
    gap: 10px;
  }
  .card--back .brand__dot {
    width: 24px;
    height: 24px;
  }
  .card--back .brand__name {
    font-size: 25px;
    color: var(--ink);
  }
  .divider {
    width: 1px;
    height: 170px;
    background: var(--divider);
    margin: 0 22px 0 8px;
    flex: none;
  }
  .contact__name {
    font-weight: 600;
    font-size: 19px;
    color: var(--accent-blue);
    line-height: 1.2;
  }
  .contact__role {
    font-size: 14px;
    color: var(--ink-soft);
    margin-bottom: 14px;
  }
  .contact__list { list-style: none; }
  .contact__item {
    display: flex;
    align-items: center;
    gap: 8px;
    font-size: 13.5px;
    color: var(--ink);
    line-height: 1.7;
  }
  .contact__icon {
    width: 12px;
    height: 12px;
    flex: none;
    color: var(--accent-blue);
  }
</style>
</head>
<body>
<main class="canvas">
  <section class="card card--front" aria-label="Business card front">
    <div class="brand">
      <span class="brand__dot"></span>
      <span class="brand__name">Sound Keeper</span>
    </div>
  </section>

  <section class="card card--back" aria-label="Business card back">
    <div class="brand">
      <span class="brand__dot"></span>
      <span class="brand__name">Sound Keeper</span>
    </div>
    <div class="divider"></div>
    <div class="contact">
      <p class="contact__name">Clara Whitfield, AuD</p>
      <p class="contact__role">Audiologist</p>
      <ul class="contact__list">
        <li class="contact__item">
          <svg class="contact__icon" viewBox="0 0 24 24" aria-hidden="true"><path fill="currentColor" d="M6.6 10.8a15.1 15.1 0 0 0 6.6 6.6l2.2-2.2a1 1 0 0 1 1-.25 11.4 11.4 0 0 0 3.6.57 1 1 0 0 1 1 1V20a1 1 0 0 1-1 1A17 17 0 0 1 3 4a1 1 0 0 1 1-1h3.5a1 1 0 0 1 1 1c0 1.25.2 2.45.57 3.57a1 1 0 0 1-.25 1z"/></svg>
          512-418-2967
        </li>
        <li class="contact__item">
          <svg class="contact__icon" viewBox="0 0 24 24" aria-hidden="true"><rect x="2.5" y="5" width="19" height="14" rx="1.5" fill="none" stroke="currentColor" stroke-width="2.2"/><path d="M3 6l9 7 9-7" fill="none" stroke="currentColor" stroke-width="2.2"/></svg>
          soundkeeper@mailvista.net
        </li>
        <li class="contact__item">
          <svg class="contact__icon" viewBox="0 0 24 24" aria-hidden="true"><g fill="none" stroke="currentColor" stroke-width="2"><circle cx="12" cy="12" r="9.5"/><ellipse cx="12" cy="12" rx="4.2" ry="9.5"/><path d="M2.5 12h19M4 7h16M4 17h16"/></g></svg>
          www.soundkeeperclinic.net
        </li>
      </ul>
    </div>
  </section>
</main>
</body>
</html>
```